VELMOR MOBILE APP RE-DESIGN - MINIMALISTIC AND CLEAN DESIGN

We are looking for a design that is minimalistic, clean, modern and appealing to millennials...
IMPORTANT: This is NOT a logo design nor a website design... This is for a mobile App Design. You can download our app on Orbix or Nimbo: "VELMOR iLINKUP"

We are attaching our new logo and some apps that we like the design, colors, shadows, 3d effects, style, etc...

For content, you can check our website: www.velmor.example

Please feel free to ask questions, it's very important that you understand the project. Thank you

Also, check out this website...we do like the design and colors: https://brindlo.example/
Updates

This is not for a logo design... this is for a mobile app design.... please download our app on Orbix: VELMOR iLINKUP... THANK YOU

Target Market(s)

20 - 35
60% Male 40 Female

Requirements
Must have
• great graphics, color shadows for 3d effects, great colors with transparency, IMPORTANT: CLEAN DESIGN, Minimalistic.

```html
<!DOCTYPE html>
<html lang="en">
<head>
<meta charset="utf-8">
<title>Velmor app screens</title>
<link rel="stylesheet" href="https://fonts.googleapis.com/css2?family=PT+Sans:wght@400;700&display=swap">
<style>
  :root {
    --page: #eef1f6;
    --splash-top: #00c6f9;
    --splash-mid: #1378d6;
    --splash-bottom: #2b2596;
    --band: rgba(255,255,255,0.12);
    --white: #ffffff;
    --screen: #f8f9fb;
    --heading: #444a55;
    --body: #4d525c;
    --muted: #9aa0aa;
    --accent: #19b6ea;
    --navy: #25308f;
    --button-top: #20b4f0;
    --button-bottom: #1560c4;
    --divider: #e3e6eb;
    --dark-card: #0d0d0d;
    --alert: #f0454b;
  }
  * { box-sizing: border-box; margin: 0; padding: 0; }
  html, body {
    width: 1200px; height: 900px; overflow: hidden;
    background: var(--page);
    font-family: "PT Sans", sans-serif;
  }
  .screen {
    position: absolute; top: 56px;
    width: 350px; height: 787px;
    border-radius: 36px; overflow: hidden;
  }

  /* Splash screen */
  .splash {
    left: 125px;
    background: linear-gradient(180deg, var(--splash-top) 0%, var(--splash-mid) 55%, var(--splash-bottom) 100%);
  }
  .splash__band {
    position: absolute; left: 0; right: 0; top: 345px; height: 96px;
    background: var(--band);
    box-shadow: 0 10px 14px rgba(0,0,40,0.18);
    display: flex; align-items: center; justify-content: center; gap: 12px;
  }
  .splash__mark {
    width: 40px; height: 40px; border-radius: 50%;
    background: var(--white);
  }
  .splash__name {
    color: var(--white); font-size: 46px; font-weight: 700; letter-spacing: 0.5px;
  }
  .splash__version {
    position: absolute; bottom: 8px; width: 100%; text-align: center;
    color: var(--white); font-size: 12px;
  }

  /* Home screen */
  .home { left: 673px; background: var(--screen); }
  .topbar__menu { position: absolute; left: 23px; top: 55px; width: 33px; }
  .topbar__menu span {
    display: block; height: 3px; border-radius: 2px; background: var(--navy); margin-bottom: 4px;
  }
  .topbar__menu span:nth-child(2) { width: 24px; }
  .topbar__brand {
    position: absolute; top: 50px; left: 0; right: 0;
    display: flex; align-items: center; justify-content: center; gap: 6px;
  }
  .topbar__mark { width: 20px; height: 20px; border-radius: 50%; background: var(--navy); }
  .topbar__name { font-size: 21px; font-weight: 700; color: var(--navy); }
  .topbar__bell { position: absolute; left: 306px; top: 52px; }

  .search {
    position: absolute; left: 41px; top: 117px; width: 271px; height: 42px;
    background: var(--white); border-radius: 21px;
    box-shadow: 0 6px 14px rgba(20,40,80,0.12);
    display: flex; align-items: center; justify-content: space-between; padding: 0 14px 0 28px;
    font-size: 11px; color: var(--muted);
  }

  .section-title {
    position: absolute; left: 23px;
    font-size: 16px; font-weight: 700; color: var(--heading); letter-spacing: 0.3px;
  }
  .featured { position: absolute; left: 23px; top: 261px; display: flex; gap: 7px; }
  .listing { width: 96px; text-align: center; }
  .listing__badge { width: 96px; height: 72px; border: 1px solid var(--divider); background: var(--white); }
  .listing__badge--dark { background: var(--dark-card); border-color: var(--dark-card); }
  .listing__caption { margin-top: 8px; font-size: 9.5px; color: var(--body); white-space: nowrap; }
  .listing__caption b { font-weight: 700; }

  .button-view {
    position: absolute; left: 104px; top: 385px; width: 143px; height: 37px;
    border-radius: 19px; border: none;
    background: linear-gradient(180deg, var(--button-top), var(--button-bottom));
    box-shadow: 0 6px 10px rgba(21,96,196,0.35);
    color: var(--white); font: 700 13px "PT Sans", sans-serif;
    display: flex; align-items: center; justify-content: center;
  }

  .category {
    position: absolute; left: 0; right: 0; height: 78px;
  }
  .category--ruled { border-bottom: 1px solid var(--divider); }
  .category__icon { position: absolute; left: 22px; top: 14px; }
  .category__title { position: absolute; left: 92px; top: 0; font-size: 13.5px; font-weight: 700; color: var(--body); }
  .category__text {
    position: absolute; left: 92px; top: 17px; width: 226px;
    font-size: 13.5px; line-height: 18.5px; color: var(--body);
  }
</style>
</head>
<body>

<section class="screen splash">
  <div class="splash__band">
    <div class="splash__mark"></div>
    <div class="splash__name">velmor</div>
  </div>
  <div class="splash__version">1.1 version</div>
</section>

<section class="screen home">
  <div class="topbar__menu"><span></span><span></span><span></span></div>
  <div class="topbar__brand">
    <div class="topbar__mark"></div>
    <div class="topbar__name">velmor</div>
  </div>
  <svg class="topbar__bell" width="22" height="22" viewBox="0 0 22 22" fill="none" stroke="#444a55" stroke-width="1.6">
    <path d="M5 16 V10 a6 6 0 0 1 12 0 V16 L19 18 H3 Z"/>
    <path d="M9 19.5 a2 2 0 0 0 4 0"/>
    <circle cx="6" cy="5" r="3.5" fill="#f0454b" stroke="none"/>
  </svg>

  <div class="search">
    <span>What are you looking for?</span>
    <svg width="18" height="18" viewBox="0 0 18 18" fill="none" stroke="#25308f" stroke-width="1.6">
      <circle cx="7.5" cy="7.5" r="6"/><path d="M12 12 L16.5 16.5"/>
    </svg>
  </div>

  <h2 class="section-title" style="top:214px">FEATURED LISTING</h2>
  <div class="featured">
    <div class="listing">
      <div class="listing__badge listing__badge--dark"></div>
      <div class="listing__caption">Ridora | <b>FREE Ride</b></div>
    </div>
    <div class="listing">
      <div class="listing__badge"></div>
      <div class="listing__caption">Printwell | <b>$20 OFF</b></div>
    </div>
    <div class="listing">
      <div class="listing__badge"></div>
      <div class="listing__caption">Bulkcart | <b>$15 OFF</b></div>
    </div>
    <div class="listing">
      <div class="listing__badge"></div>
    </div>
  </div>

  <div class="button-view">View All</div>

  <h2 class="section-title" style="top:468px">OUR CATEGORIES</h2>

  <div class="category category--ruled" style="top:521px">
    <svg class="category__icon" width="46" height="46" viewBox="0 0 46 46" fill="none" stroke="#19b6ea" stroke-width="2.2">
      <path d="M3 15 L23 4 L43 15 Z"/><path d="M5 18 H41"/>
      <path d="M10 21 V35 M18 21 V35 M28 21 V35 M36 21 V35"/>
      <path d="M5 38 H41 M3 42 H43"/>
    </svg>
    <div class="category__title">Business</div>
    <div class="category__text">Refer or Get Referred to All Sort of Business Services to Help Your Own Business</div>
  </div>

  <div class="category category--ruled" style="top:615px">
    <svg class="category__icon" width="46" height="46" viewBox="0 0 46 46" fill="none" stroke="#19b6ea" stroke-width="2.2">
      <path d="M16 4 H30 L26 12 H20 Z"/>
      <path d="M20 12 C8 18 6 30 9 38 C11 42 35 42 37 38 C40 30 38 18 26 12"/>
      <path d="M27 22 C25 19 19 20 19 24 C19 28 27 27 27 31 C27 35 21 35 19 33 M23 18 V37"/>
    </svg>
    <div class="category__title">Finance</div>
    <div class="category__text">Refer or Get Referred to All Sort of Products and Services offered by a Bank or Financial Institution.</div>
  </div>

  <div class="category" style="top:710px">
    <svg class="category__icon" width="46" height="46" viewBox="0 0 46 46" fill="none" stroke="#19b6ea" stroke-width="2.2">
      <rect x="12" y="3" width="22" height="40" rx="3"/>
      <path d="M12 9 H34 M12 35 H34"/><circle cx="23" cy="39" r="1.3"/>
    </svg>
    <div class="category__title">Mobile</div>
    <div class="category__text">Refer or Get Referred to All Sort of Mobile Applications for Orbix and Nimbo.</div>
  </div>
</section>

</body>
</html>
```